Logo design and Businesscard and letterhead for Technology Company

We need logo design for a new company based in Atlanta called "Vornimel". We provide information about technology Product and service provider companies, information about their Products and services. Our initial focus is to List various companies and their products, various consulting companies and their services. We want to convey the message that this will be one stop shop to find out all the information to make smart technology decisions

I am looking for Logo, Business Card and Letterhead.

Target Market(s)

Companies that have IT department, IT users such as Developers, Managers, C level, Technology Product companies , Consulting companies and service providers.

Industry/Entity Type

It Company

Requirements
Must have
• Looking for some Unique design idea.
Nice to have
• I want something that connects information across technologies between technology buyers and sellers.
Should not have
• No puzzle design.

```html
<!DOCTYPE html>
<html lang="en">
<head>
<meta charset="utf-8">
<title>Vornimel — Stationery Set</title>
<link href="https://fonts.googleapis.com/css2?family=Questrial&family=Oswald:wght@300;500&display=swap" rel="stylesheet">
<style>
  :root {
    --navy: #1b1464;
    --orange: #f47a36;
    --green: #4aac45;
    --grey-text: #8a8a96;
    --rule: #c9c9cf;
    --card-light: #e4e3ef;
    --card-ornament-dark: #2f2a82;
    --card-ornament-light: #dcdbea;
    --paper: #ffffff;
  }
  * { box-sizing: border-box; margin: 0; padding: 0; }
  html, body { width: 871px; height: 1200px; overflow: hidden; background: var(--paper); }
  .sheet { position: relative; width: 871px; height: 1200px; }
  .trim, .footer-swoosh { position: absolute; inset: 0; }
  .brand {
    position: absolute; left: 0; right: 0; display: flex; justify-content: center; align-items: center; gap: 12px;
    font-family: "Questrial", sans-serif; color: var(--navy); letter-spacing: 2px; font-size: 40px; line-height: 1;
  }
  .brand-dot { flex: none; border-radius: 50%; background: var(--orange); }
  .brand .brand-dot { width: 30px; height: 30px; }
  .brand--header { top: 106px; }
  .brand--centre { top: 484px; }
  .contact-line {
    position: absolute; top: 194px; left: 0; right: 0; text-align: center; white-space: nowrap;
    font-family: "Oswald", sans-serif; font-weight: 300; font-size: 12.5px; color: var(--grey-text); letter-spacing: 0.6px;
  }
  .contact-line b { font-weight: 500; color: var(--navy); }
  .contact-line .sep { color: var(--orange); margin: 0 6px; }
  .card { position: absolute; top: 643px; width: 269px; height: 163px; border-radius: 8px; overflow: hidden; }
  .card--front { left: 168px; background: var(--navy); }
  .card--back { left: 462px; background: var(--card-light); }
  .card svg { position: absolute; inset: 0; }
  .card-ornament { position: absolute; border-radius: 30px; }
  .card--front .card-ornament { left: 12px; top: 8px; width: 62px; height: 142px; background: var(--card-ornament-dark); }
  .card--back .card-ornament { left: 40px; top: 16px; width: 76px; height: 112px; background: var(--card-ornament-light); }
  .card-brand { position: absolute; display: flex; align-items: center; gap: 6px; font-family: "Questrial", sans-serif; letter-spacing: 1px; line-height: 1; }
  .card-brand .brand-dot { width: 16px; height: 16px; }
  .card--front .card-brand { left: 78px; top: 46px; font-size: 20px; color: var(--paper); }
  .card--back .card-brand { left: 20px; top: 10px; font-size: 17px; color: var(--navy); }
  .card-holder { position: absolute; left: 33px; top: 97px; font-family: "Oswald", sans-serif; font-size: 8.5px; color: var(--grey-text); font-weight: 300; white-space: nowrap; }
  .card-holder b { color: var(--navy); font-weight: 500; }
  .card-contact { position: absolute; right: 8px; bottom: 5px; font-family: "Oswald", sans-serif; font-size: 6.5px; color: var(--grey-text); font-weight: 300; white-space: nowrap; }
  .card-contact b { color: var(--navy); font-weight: 500; }
</style>
</head>
<body>
<main class="sheet">
  <svg class="trim" viewBox="0 0 871 1200" width="871" height="1200" aria-hidden="true">
    <g stroke="var(--rule)" stroke-width="1" fill="none">
      <rect x="44" y="44" width="786" height="1116"/>
      <line x1="0" y1="44" x2="30" y2="44"/><line x1="44" y1="0" x2="44" y2="30"/>
      <line x1="841" y1="44" x2="871" y2="44"/><line x1="830" y1="0" x2="830" y2="30"/>
      <line x1="0" y1="1160" x2="30" y2="1160"/><line x1="44" y1="1170" x2="44" y2="1200"/>
      <line x1="841" y1="1160" x2="871" y2="1160"/><line x1="830" y1="1170" x2="830" y2="1200"/>
    </g>
  </svg>

  <div class="brand brand--header"><span class="brand-dot"></span>Vornimel</div>
  <p class="contact-line">
    <b>Tel:</b> 00 987 60214<span class="sep">|</span><b>Fax:</b> 00 987 60215<span class="sep">|</span><b>E-mail</b> : info@vornimel.com<span class="sep">|</span><b>Website</b> : www.vornimel.com<span class="sep">|</span><b>Location</b> : Lakeview, USA.
  </p>

  <div class="brand brand--centre"><span class="brand-dot"></span>Vornimel</div>

  <section class="card card--front">
    <div class="card-ornament" role="img" aria-label="Faint floral flourish ornament"></div>
    <svg viewBox="0 0 269 163" width="269" height="163" aria-hidden="true">
      <path d="M8 156 Q190 150 269 72 L269 96 Q195 146 8 156 Z" fill="var(--orange)"/>
      <path d="M8 156 Q195 146 269 96 L269 114 Q200 154 8 156 Z" fill="var(--green)"/>
    </svg>
    <div class="card-brand"><span class="brand-dot"></span>Vornimel</div>
  </section>

  <section class="card card--back">
    <div class="card-ornament" role="img" aria-label="Faint floral flourish ornament"></div>
    <svg viewBox="0 0 269 163" width="269" height="163" aria-hidden="true">
      <path d="M8 148 Q190 140 269 68 L269 88 Q195 136 8 148 Z" fill="var(--orange)"/>
      <path d="M8 148 Q195 136 269 88 L269 102 Q200 144 8 148 Z" fill="var(--green)"/>
    </svg>
    <div class="card-brand"><span class="brand-dot"></span>Vornimel</div>
    <p class="card-holder"><b>Name of the Owner</b> | Designation</p>
    <p class="card-contact"><b>Tel:</b> 00 987 60214, <b>Fax:</b> 00 987 60215, <b>E-mail:</b> info@vornimel.com</p>
  </section>

  <svg class="footer-swoosh" viewBox="0 0 871 1200" width="871" height="1200" aria-hidden="true">
    <path d="M46 1158 Q620 1125 830 917 L830 977 Q615 1132 46 1158 Z" fill="var(--orange)"/>
    <path d="M46 1158 Q615 1132 830 977 L830 1004 Q630 1148 46 1158 Z" fill="var(--green)"/>
  </svg>
</main>
</body>
</html>
```